Harborline Finish Works business cards

we sandblast, power tool, and paint Navy ships and steel structures. When we paint we use brushes, rollers, and airless sprayers. We do marine work as well as industrial. Some things that are important for our customer to know is Quality, Safety, Excellence, Dependability and Professional. We definitely would like to have our company logo that was designed here on art kiosk incorporated into the business card. We are open for suggestions as far as the design goes.

Target Market(s)

marine and industrial

Industry/Entity Type

Painting

Contact Information for Business Card

Derek Mallow
612-385-2049
dmallow@hlfworks.example

Font styles to use
Serif
Decorative
Script

Colors
fbed22
000000
ffffff

Requirements
Must have
• company logo that is uploaded

```html
<!DOCTYPE html>
<html lang="en">
<head>
<meta charset="utf-8">
<title>Harborline Finish Works – Business Cards</title>
<link href="https://fonts.googleapis.com/css2?family=Cinzel:wght@700&family=Cormorant+Garamond:wght@500&display=swap" rel="stylesheet">
<style>
  :root{
    --backdrop:#2b2b2d;
    --card-black:#0d0d0e;
    --card-black-soft:#1a1a1c;
    --gold:#e0b64a;
    --steel:#8d8f94;
    --steel-light:#b9bbbf;
  }
  *{margin:0;padding:0;box-sizing:border-box}
  html,body{width:1200px;height:660px;overflow:hidden;background:var(--backdrop)}
  .canvas{position:relative;width:1200px;height:660px;display:flex;align-items:center;justify-content:center;gap:50px}
  .card{position:relative;width:530px;height:303px;background:linear-gradient(160deg,var(--card-black-soft),var(--card-black) 60%);overflow:hidden;box-shadow:0 14px 30px rgba(0,0,0,.45)}
  .card__bands{position:absolute;inset:0;width:100%;height:100%}
  .brand{position:absolute;display:flex;align-items:center;gap:12px}
  .brand__mark{width:34px;height:34px;border:3px solid var(--gold);border-radius:50%;flex:none}
  .brand__name{font-family:"Cinzel",serif;font-weight:700;color:var(--gold);line-height:1.05;letter-spacing:.5px}
  .brand__name span{display:block}
  .card--front .brand{left:50%;top:50%;transform:translate(-50%,-50%)}
  .card--front .brand__name{font-size:32px}
  .card--front .brand__name span+span{font-size:17px;letter-spacing:3px}
  .card--back .brand{left:34px;top:128px}
  .card--back .brand__name{font-size:24px}
  .card--back .brand__name span+span{font-size:13px;letter-spacing:2.5px}
  .divider{position:absolute;left:282px;top:70px;width:1px;height:150px;background:var(--steel);opacity:.45}
  .contact{position:absolute;left:302px;top:100px;font-family:"Cormorant Garamond",serif;font-weight:500;color:var(--steel-light)}
  .contact__name{font-family:"Cinzel",serif;font-weight:700;color:var(--gold);font-size:19px;letter-spacing:1px;margin-bottom:10px}
  .contact__row{display:flex;align-items:center;gap:8px;font-size:16px;margin-bottom:4px}
  .contact__row svg{width:13px;height:13px;flex:none}
</style>
</head>
<body>
<main class="canvas">

  <section class="card card--front" aria-label="Card front">
    <svg class="card__bands" viewBox="0 0 530 303" preserveAspectRatio="none" aria-hidden="true">
      <polygon points="0,0 250,0 236,16 0,16" fill="var(--gold)"/>
      <polygon points="250,0 420,0 412,8 242,8" fill="var(--steel)" opacity=".7"/>
      <polygon points="0,22 210,22 206,26 0,26" fill="var(--steel)" opacity=".6"/>
      <polygon points="530,303 280,303 294,287 530,287" fill="var(--gold)"/>
      <polygon points="280,303 110,303 118,295 288,295" fill="var(--steel)" opacity=".7"/>
      <polygon points="530,281 320,281 324,277 530,277" fill="var(--steel)" opacity=".6"/>
    </svg>
    <div class="brand">
      <span class="brand__mark"></span>
      <p class="brand__name"><span>Harborline</span><span>Finish Works</span></p>
    </div>
  </section>

  <section class="card card--back" aria-label="Card back">
    <svg class="card__bands" viewBox="0 0 530 303" preserveAspectRatio="none" aria-hidden="true">
      <polygon points="260,0 530,0 530,10 270,10" fill="var(--steel)" opacity=".7"/>
      <polygon points="300,16 530,16 530,20 304,20" fill="var(--steel)" opacity=".5"/>
      <polygon points="530,303 250,303 266,283 530,283" fill="var(--gold)"/>
      <polygon points="250,303 60,303 68,295 258,295" fill="var(--steel)" opacity=".7"/>
      <circle cx="410" cy="130" r="70" fill="none" stroke="var(--steel)" stroke-width="6" opacity=".08"/>
    </svg>
    <div class="brand">
      <span class="brand__mark"></span>
      <p class="brand__name"><span>Harborline</span><span>Finish Works</span></p>
    </div>
    <div class="divider"></div>
    <div class="contact">
      <p class="contact__name">DEREK MALLOW</p>
      <p class="contact__row">
        <svg viewBox="0 0 12 12" aria-hidden="true"><rect x="3" y="0.5" width="6" height="11" rx="1" fill="none" stroke="var(--gold)" stroke-width="1.2"/></svg>
        612-385-2049
      </p>
      <p class="contact__row">
        <svg viewBox="0 0 12 12" aria-hidden="true"><rect x="0.5" y="2" width="11" height="8" fill="var(--gold)"/><polyline points="0.5,2 6,7 11.5,2" fill="none" stroke="var(--card-black)" stroke-width="1"/></svg>
        dmallow@hlfworks.example
      </p>
    </div>
  </section>

</main>
</body>
</html>
```